Harrows Menu Design for a sports bar concept

We need an updated look for this current menu design, 8.5x16". It's a sports bar concept. We like the wood planks at the top header but need to do something with the white space.

Target Market(s)

ages 20-40s. Social drinkers.

Industry/Entity Type

Sports Bar

Font styles to use
Sans Serif

Colors
f58b49
3176b5
0355a3
ec1f27

Requirements
Must have
• Cannot change logo.
Nice to have
• Similar fonts if possible.
• Titles: Asphaltum WF
• Descriptions: Akzidenz Grotesk Roman

```html
<!DOCTYPE html>
<html lang="en">
<head>
<meta charset="utf-8">
<title>Harrows Grill Menu</title>
<link rel="stylesheet" href="https://fonts.googleapis.com/css2?family=Oswald:wght@500;700&family=Roboto:ital,wght@0,400;0,700;1,400&family=Kalam:wght@700&display=swap">
<style>
  :root{
    --navy:#0b2857;
    --blue:#0355a3;
    --sky:#3176b5;
    --red:#ec1f27;
    --orange:#f58b49;
    --green:#3d8a2e;
    --brown:#5a3320;
    --chili:#b01f28;
    --paper:#eef0f3;
    --ink:#2b2b2b;
    --wood-dark:#4a2a16;
    --wood-mid:#7a4a28;
    --wood-light:#9a6438;
  }
  *{box-sizing:border-box}
  html,body{margin:0;width:1200px;height:2216px;overflow:hidden}
  body{background:var(--paper);font-family:'Roboto',Arial,sans-serif;color:var(--ink);position:relative}

  /* header */
  .masthead{position:absolute;left:0;top:0;width:1200px;height:360px;
    background:linear-gradient(180deg,var(--wood-light) 0%,var(--wood-mid) 45%,var(--wood-dark) 100%);
    border-bottom:8px solid var(--red);display:flex;flex-direction:column;align-items:center;justify-content:center}
  .brand-name,.brand-sub{font-family:'Oswald',Impact,sans-serif;font-weight:700;color:#fff;text-transform:uppercase;margin:0;line-height:1}
  .brand-name{font-size:150px;letter-spacing:4px}
  .brand-sub{font-size:56px;letter-spacing:14px;margin-top:8px}

  /* section headings */
  .section-head{position:absolute;left:0;height:56px;display:flex;align-items:center;gap:14px}
  .section-head svg{width:34px;height:56px;display:block}
  .section-head h2{margin:0;font:700 54px/1 'Oswald',Impact,sans-serif;text-transform:uppercase;color:var(--navy);letter-spacing:1px}
  .salads .section-head h2{color:var(--green)}
  .sandwiches .section-head h2{color:var(--brown)}
  .mexican .section-head h2{color:var(--chili)}

  .appetizers{--accent:var(--blue)}
  .salads{--accent:var(--green)}
  .sandwiches{--accent:var(--brown)}
  .mexican{--accent:var(--chili)}

  /* cards */
  .card{position:absolute;display:flex;flex-direction:column;background:#fff;box-shadow:0 2px 6px rgba(0,0,0,.25);overflow:hidden}
  .card .photo{flex:1 1 auto;position:relative;min-height:60px}
  .card-title{margin:0;background:var(--accent);color:#fff;font:700 20px/1.1 'Oswald',Impact,sans-serif;text-transform:uppercase;padding:7px 10px;flex:none}
  .card-title small{font-size:14px;font-weight:500}
  .card-desc{margin:0;padding:6px 10px 9px;font:13px/1.3 'Roboto',Arial,sans-serif;color:var(--ink);flex:none}
  .star-badge{position:absolute;left:0;top:0;width:46px;height:46px;z-index:2}
  .card--wide{flex-direction:row}
  .card--wide .photo{flex:0 0 300px}
  .card--wide .card-body{flex:1;display:flex;flex-direction:column;justify-content:center}

  /* appetizer tiles */
  .tile{position:absolute;width:176px;height:132px;box-shadow:0 2px 5px rgba(0,0,0,.25);overflow:hidden}
  .tile .photo{position:absolute;inset:0}
  .tile-label{position:absolute;left:0;bottom:10px;max-width:100%;background:var(--accent);color:#fff;
    font:700 18px/1.1 'Oswald',Impact,sans-serif;text-transform:uppercase;padding:5px 9px;margin:0}
  .tile-label small{font-size:12px;font-weight:500}
  .tile--top .tile-label{top:10px;bottom:auto}

  /* food photo fills */
  .photo--dip{background:radial-gradient(circle at 40% 45%,#fbfaf4 0 28%,#f3a35c 29% 48%,#7cae4a 49% 70%,#e9e3d6 71%)}
  .photo--fried{background:radial-gradient(circle at 50% 50%,#f2c66a 0 35%,#c98a33 60%,#7d4d1d 100%)}
  .photo--salad{background:radial-gradient(circle at 45% 50%,#e9efdf 0 18%,#8cbd52 40%,#4d8a2c 75%,#2f5c1c 100%)}
  .photo--sandwich{background:radial-gradient(circle at 50% 50%,#e7c58b 0 30%,#b47b3e 60%,#6b3f1e 100%)}
  .photo--nachos{background:radial-gradient(circle at 50% 50%,#f6dc74 0 30%,#e39a3b 55%,#8e4e1c 100%)}
  .photo--meat{background:radial-gradient(circle at 50% 50%,#b8462c 0 30%,#7a2a1a 65%,#d8cfc4 100%)}

  .served-with{position:absolute;left:32px;top:1326px;margin:0;font:italic 18px/1 'Roboto',Arial,sans-serif;color:var(--navy)}

  /* social + note */
  .social{position:absolute;left:412px;top:2026px;display:flex;align-items:center;gap:12px}
  .social-square{width:40px;height:40px;border-radius:6px;background:var(--sky)}
  .social-square:nth-child(2){background:var(--blue)}
  .social-square:nth-child(3){background:var(--red)}
  .hashtag{font:700 30px/1 'Oswald',Impact,sans-serif;color:var(--navy);margin-left:8px}
  .site{position:absolute;left:412px;top:2084px;margin:0;font:700 24px/1 'Roboto',Arial,sans-serif;color:var(--blue)}
  .specials-note{position:absolute;left:900px;top:2020px;width:270px;height:122px;background:#fffdf6;
    box-shadow:0 3px 8px rgba(0,0,0,.3);transform:rotate(-3deg);padding:14px 18px;margin:0;
    font:700 23px/1.2 'Kalam','Comic Sans MS',cursive;color:var(--chili)}

  .footer-bar{position:absolute;left:0;top:2152px;width:1200px;height:64px;background:var(--navy);
    color:#fff;display:flex;align-items:center;padding:0 32px;font:16px/1 'Roboto',Arial,sans-serif;margin:0}
</style>
</head>
<body>

<svg width="0" height="0" style="position:absolute" aria-hidden="true">
  <defs>
    <symbol id="star-badge" viewBox="0 0 46 46">
      <rect width="46" height="46" fill="#0b2857"/>
      <polygon points="23,8 27.4,18.6 38.8,19.4 30.1,26.8 32.8,37.9 23,31.9 13.2,37.9 15.9,26.8 7.2,19.4 18.6,18.6" fill="#fff"/>
    </symbol>
    <symbol id="flag-strip" viewBox="0 0 34 56">
      <rect width="34" height="56" fill="#fff"/>
      <rect y="0" width="34" height="8" fill="#ec1f27"/>
      <rect y="16" width="34" height="8" fill="#ec1f27"/>
      <rect y="32" width="34" height="8" fill="#ec1f27"/>
      <rect y="48" width="34" height="8" fill="#ec1f27"/>
      <rect width="20" height="24" fill="#0355a3"/>
      <polygon points="10,5 11.8,10 17,10 12.8,13 14.4,18 10,15 5.6,18 7.2,13 3,10 8.2,10" fill="#fff"/>
    </symbol>
  </defs>
</svg>

<header class="masthead" role="img" aria-label="Wooden plank header with the Harrows Grill name">
  <p class="brand-name">Harrows</p>
  <p class="brand-sub">Grill</p>
</header>

<!-- Appetizers -->
<section class="appetizers">
  <div class="section-head" style="top:376px">
    <svg><use href="#flag-strip"/></svg>
    <h2>Appetizers</h2>
  </div>

  <div class="tile tile--top" style="left:32px;top:440px"><div class="photo photo--dip" role="img" aria-label="Carrot and celery sticks with dip"></div><p class="tile-label">Carrots &amp; Celery</p></div>
  <div class="tile" style="left:216px;top:440px"><div class="photo photo--fried" role="img" aria-label="Basket of french fries"></div><p class="tile-label">French Fries</p></div>
  <div class="tile tile--top" style="left:32px;top:580px"><div class="photo photo--fried" role="img" aria-label="Chili cheese fries"></div><p class="tile-label">Chili Cheese Fries</p></div>
  <div class="tile" style="left:216px;top:580px"><div class="photo photo--fried" role="img" aria-label="Onion rings"></div><p class="tile-label">Onion Rings</p></div>
  <div class="tile tile--top" style="left:32px;top:720px"><div class="photo photo--fried" role="img" aria-label="Chicken tenders"></div><p class="tile-label">Chicken Tenders</p></div>
  <div class="tile" style="left:216px;top:720px"><div class="photo photo--fried" role="img" aria-label="Mozzarella sticks"></div><p class="tile-label">Mozzarella Sticks <small>6pcs</small></p></div>
  <div class="tile tile--top" style="left:32px;top:860px"><div class="photo photo--meat" role="img" aria-label="Buffalo wings"></div><p class="tile-label">Buffalo or BBQ Wings</p></div>
  <div class="tile" style="left:216px;top:860px"><div class="photo photo--nachos" role="img" aria-label="Loaded potato skins"></div><p class="tile-label">Loaded Potato Skins <small>4pcs</small></p></div>

  <article class="card" style="left:412px;top:440px;width:248px;height:220px">
    <svg class="star-badge"><use href="#star-badge"/></svg>
    <div class="photo photo--meat" role="img" aria-label="Meatballs in marinara"></div>
    <h3 class="card-title">Handmade Meatballs <small>-6ea</small></h3>
    <p class="card-desc">ground beef / spices / marinara / garlic bread</p>
  </article>
  <article class="card" style="left:674px;top:440px;width:248px;height:220px">
    <svg class="star-badge"><use href="#star-badge"/></svg>
    <div class="photo photo--meat" role="img" aria-label="Jumbo chicken wings"></div>
    <h3 class="card-title">Harrows Jumbo Cut Wings</h3>
    <p class="card-desc">buffalo, bbq or teriyaki pepper / 6 or 12 pcs</p>
  </article>
  <article class="card" style="left:936px;top:440px;width:248px;height:220px">
    <svg class="star-badge"><use href="#star-badge"/></svg>
    <div class="photo photo--nachos" role="img" aria-label="Chips with salsa"></div>
    <h3 class="card-title">Fresh Made Chips</h3>
    <p class="card-desc">homemade salsa or guacamole</p>
  </article>
  <article class="card" style="left:412px;top:672px;width:248px;height:206px">
    <svg class="star-badge"><use href="#star-badge"/></svg>
    <div class="photo photo--nachos" role="img" aria-label="Loaded nachos"></div>
    <h3 class="card-title">Loaded Nachos</h3>
    <p class="card-desc">chicken or steak / beans / sour cream / guacamole / salsa / jalapeño</p>
  </article>
  <article class="card" style="left:674px;top:672px;width:510px;height:206px">
    <svg class="star-badge"><use href="#star-badge"/></svg>
    <div class="photo photo--fried" role="img" aria-label="Sampler platter of appetizers"></div>
    <h3 class="card-title">Harrows Sampler Platter</h3>
    <p class="card-desc">4 buffalo wings / 4 mozzarella sticks / 4 potato skins / 2 chicken tenders</p>
  </article>
</section>

<!-- Salads -->
<section class="salads">
  <article class="card" style="left:412px;top:890px;width:248px;height:226px">
    <svg class="star-badge"><use href="#star-badge"/></svg>
    <div class="photo photo--salad" role="img" aria-label="Caesar salad"></div>
    <h3 class="card-title">Caesar</h3>
    <p class="card-desc">chicken / croutons tossed in caesar dressing</p>
  </article>
  <article class="card" style="left:674px;top:890px;width:248px;height:226px">
    <svg class="star-badge"><use href="#star-badge"/></svg>
    <div class="photo photo--salad" role="img" aria-label="Buffalo chicken salad"></div>
    <h3 class="card-title">Buffalo Chicken Salad</h3>
    <p class="card-desc">celery / tomato / avocado / breaded chicken with buffalo sauce / blue cheese dressing</p>
  </article>
  <article class="card" style="left:936px;top:890px;width:248px;height:226px">
    <svg class="star-badge"><use href="#star-badge"/></svg>
    <div class="photo photo--salad" role="img" aria-label="Balsamic salad"></div>
    <h3 class="card-title">Balsamic Salad</h3>
    <p class="card-desc">grilled chicken / bacon / blue cheese / walnuts / tomato / dried cranberries / balsamic vinaigrette</p>
  </article>

  <div class="section-head" style="top:1010px">
    <svg><use href="#flag-strip"/></svg>
    <h2>Salads</h2>
  </div>

  <article class="card" style="left:32px;top:1080px;width:176px;height:236px">
    <div class="photo photo--salad" role="img" aria-label="Grilled chicken salad"></div>
    <h3 class="card-title">Grilled Chicken Salad</h3>
    <p class="card-desc">chicken / avocado / tomatoes / croutons / dressing</p>
  </article>
  <article class="card" style="left:216px;top:1080px;width:176px;height:236px">
    <div class="photo photo--salad" role="img" aria-label="House salad"></div>
    <h3 class="card-title">Harrows House Salad</h3>
    <p class="card-desc">croutons / tomatoes / dressing</p>
  </article>
  <article class="card card--wide" style="left:412px;top:1128px;width:772px;height:188px">
    <div class="photo photo--salad" role="img" aria-label="Cobb salad"></div>
    <div class="card-body">
      <h3 class="card-title">The Country Cobb</h3>
      <p class="card-desc">grilled chicken / bacon / chopped egg / blue cheese crumbles / baby heirloom tomatoes / avocado / ranch dressing</p>
    </div>
  </article>
</section>

<p class="served-with">served with french fries, sweet potato fries, onion or a small house salad</p>

<!-- Sandwiches -->
<section class="sandwiches">
  <div class="section-head" style="top:1360px">
    <svg><use href="#flag-strip"/></svg>
    <h2>Sandwiches</h2>
  </div>

  <article class="card" style="left:32px;top:1428px;width:220px;height:182px">
    <div class="photo photo--sandwich" role="img" aria-label="BBQ grilled cheese sandwich"></div>
    <h3 class="card-title">BBQ Grilled Cheese</h3>
    <p class="card-desc">texas toast / bacon / american cheese / bbq sauce</p>
  </article>
  <article class="card" style="left:265px;top:1428px;width:220px;height:182px">
    <div class="photo photo--sandwich" role="img" aria-label="Grilled chicken chipotle sandwich"></div>
    <h3 class="card-title">Grilled Chicken Chipotle</h3>
    <p class="card-desc">pepper jack cheese / avocado / lettuce / brioche bun</p>
  </article>
  <article class="card" style="left:498px;top:1428px;width:220px;height:182px">
    <div class="photo photo--sandwich" role="img" aria-label="Grilled chicken club sandwich"></div>
    <h3 class="card-title">Grilled Chicken Club</h3>
    <p class="card-desc">bacon / lettuce / tomato / mayo / swiss cheese / brioche bun</p>
  </article>
  <article class="card" style="left:731px;top:1428px;width:220px;height:182px">
    <div class="photo photo--sandwich" role="img" aria-label="Roast beef sandwich"></div>
    <h3 class="card-title">Roast Beef Sandwich</h3>
    <p class="card-desc">mayo / provolone cheese / lettuce / tomato / sub</p>
  </article>
  <article class="card" style="left:964px;top:1428px;width:220px;height:182px">
    <div class="photo photo--sandwich" role="img" aria-label="Bacon lettuce tomato sandwich"></div>
    <h3 class="card-title">Bacon Sauce ULT</h3>
    <p class="card-desc">bacon / mayo / sauce / lettuce / tomato / sourdough</p>
  </article>

  <article class="card" style="left:32px;top:1620px;width:220px;height:182px">
    <div class="photo photo--sandwich" role="img" aria-label="Turkey sandwich"></div>
    <h3 class="card-title">Turkey</h3>
    <p class="card-desc">all natural turkey / swiss / lettuce / tomato / pickle</p>
  </article>
  <article class="card" style="left:265px;top:1620px;width:220px;height:182px">
    <div class="photo photo--sandwich" role="img" aria-label="Hawaiian chicken sandwich"></div>
    <h3 class="card-title">Hawaiian Chicken</h3>
    <p class="card-desc">pineapple / grilled onions / teriyaki / swiss cheese / brioche bun</p>
  </article>
  <article class="card" style="left:498px;top:1620px;width:220px;height:182px">
    <div class="photo photo--meat" role="img" aria-label="Meatball sub"></div>
    <h3 class="card-title">Meatball</h3>
    <p class="card-desc">homemade meatballs / mozzarella / marinara served on a french roll</p>
  </article>
  <article class="card" style="left:731px;top:1620px;width:220px;height:182px">
    <div class="photo photo--sandwich" role="img" aria-label="French dip sandwich"></div>
    <h3 class="card-title">French Dip</h3>
    <p class="card-desc">choice angus top round / provolone / side of au jus on a french roll</p>
  </article>
  <article class="card" style="left:964px;top:1620px;width:220px;height:182px">
    <div class="photo photo--sandwich" role="img" aria-label="Grilled cheese sandwich"></div>
    <h3 class="card-title">Grilled Cheese</h3>
    <p class="card-desc">texas toast / american / swiss</p>
  </article>
</section>

<!-- Mexican -->
<section class="mexican">
  <div class="section-head" style="top:1818px">
    <svg><use href="#flag-strip"/></svg>
    <h2>Mexican</h2>
  </div>

  <article class="card" style="left:32px;top:1884px;width:176px;height:250px">
    <div class="photo photo--nachos" role="img" aria-label="BBQ grilled cheese quesadilla"></div>
    <h3 class="card-title">BBQ Grilled Cheese</h3>
    <p class="card-desc">texas toast / bacon / american cheese / bbq sauce</p>
  </article>
  <article class="card" style="left:216px;top:1884px;width:176px;height:250px">
    <div class="photo photo--nachos" role="img" aria-label="Grilled chicken chipotle wrap"></div>
    <h3 class="card-title">Grilled Chicken Chipotle</h3>
    <p class="card-desc">pepper jack cheese / avocado / lettuce / brioche bun</p>
  </article>
  <article class="card" style="left:412px;top:1818px;width:248px;height:190px">
    <div class="photo photo--nachos" role="img" aria-label="Grilled chicken club"></div>
    <h3 class="card-title">Grilled Chicken Club</h3>
    <p class="card-desc">bacon / lettuce / tomato / mayo / swiss cheese / brioche bun</p>
  </article>
  <article class="card" style="left:674px;top:1818px;width:248px;height:190px">
    <div class="photo photo--nachos" role="img" aria-label="Hawaiian chicken"></div>
    <h3 class="card-title">Hawaiian Chicken</h3>
    <p class="card-desc">pineapple / grilled onions / teriyaki / swiss cheese / brioche bun</p>
  </article>
  <article class="card" style="left:936px;top:1818px;width:248px;height:180px">
    <div class="photo photo--nachos" role="img" aria-label="Grilled cheese"></div>
    <h3 class="card-title">Grilled Cheese</h3>
    <p class="card-desc">texas toast / american / swiss</p>
  </article>
</section>

<div class="social">
  <span class="social-square"></span>
  <span class="social-square"></span>
  <span class="social-square"></span>
  <span class="hashtag">#harrowsgrill</span>
</div>
<p class="site">www.harrowsgrill.com</p>

<p class="specials-note">Ask about our daily specials, appetizers, sparkling, or sides.</p>

<p class="footer-bar">Harrows Grill Address: 123 Lorem impsum lolo renter memaun &nbsp; Contact Number: 123 456 789</p>

</body>
</html>
```